Birchwood Clover Business Cards

I need a business card with my logo, number, Facebook account, and some information about what I am selling. Green card with logo on the front. 555-218-3946 phone number, @birchwoodclover Facebook, •Orchardgrass Hay •Alfalfa Hay •Mixed Grass Hay , and “Premium Quality Hay” all written on the back.

Target Market(s)

Hay

Contact Information for Business Card

Phone number, Facebook, different types of hay.

Colors
00AB8E
00BBA5
67D7C9
C6EFE9
E9F9F6

```html
<!DOCTYPE html>
<html lang="en">
<head>
<meta charset="utf-8">
<title>Birchwood Clover Business Cards</title>
<link href="https://fonts.googleapis.com/css2?family=Marck+Script&family=Montserrat:wght@600&display=swap" rel="stylesheet">
<style>
  :root {
    --backdrop: #f3e6d6;
    --charcoal: #2a2a2a;
    --teal: #2bb08f;
    --teal-light: #67d7c9;
    --leaf: #1f9641;
    --paper: #f2f2f2;
    --ink: #1c1c1c;
    --white: #ffffff;
  }
  * { box-sizing: border-box; margin: 0; padding: 0; }
  html, body { width: 1200px; height: 1200px; overflow: hidden; }
  body {
    background: var(--backdrop);
    font-family: "Montserrat", sans-serif;
    position: relative;
  }
  .card {
    position: absolute;
    left: 180px;
    width: 840px;
    height: 480px;
    overflow: hidden;
    box-shadow: 0 6px 18px rgba(0,0,0,0.18);
  }
  /* Back of card */
  .card-back { top: 70px; background: var(--teal); }
  .back-band {
    position: absolute; left: 0; top: 0; width: 100%; height: 190px;
    background: var(--charcoal);
  }
  .brand-mark {
    position: absolute; left: 40px; top: 110px;
    display: flex; align-items: center; gap: 14px;
    white-space: nowrap;
  }
  .brand-dot { width: 44px; height: 44px; border-radius: 50%; background: var(--leaf); flex: none; }
  .brand-name {
    font-family: "Marck Script", cursive;
    font-size: 36px; color: var(--white);
  }
  .contact-list {
    position: absolute; left: 440px; top: 34px;
    list-style: none; display: flex; flex-direction: column; gap: 22px;
  }
  .contact-item {
    display: flex; align-items: center; gap: 18px;
    color: var(--white); font-size: 29px; font-weight: 600; letter-spacing: 0.5px;
    white-space: nowrap;
  }
  .contact-icon {
    width: 40px; height: 40px; border-radius: 50%;
    border: 2px solid var(--teal);
    display: flex; align-items: center; justify-content: center;
    flex: none;
  }
  .contact-icon svg { width: 20px; height: 20px; }
  .contact-icon.plain .inner { width: 14px; height: 14px; border-radius: 50%; background: var(--teal); }
  .watermark-art {
    position: absolute; left: 40px; top: 200px; width: 340px; height: 270px;
    border-radius: 50% 50% 0 0;
    background: radial-gradient(ellipse at 60% 60%, rgba(103,215,201,0.35), rgba(103,215,201,0) 70%);
  }
  .hay-list {
    position: absolute; left: 420px; top: 214px;
    list-style: none; color: var(--white);
  }
  .hay-item {
    font-size: 24px; font-weight: 600; line-height: 58px;
    white-space: nowrap;
  }
  .hay-item:nth-child(2) { padding-left: 24px; }
  .hay-item:nth-child(3) { padding-left: 48px; }
  .hay-item:nth-child(4) { padding-left: 72px; }
  .initial {
    font-family: "Marck Script", cursive; font-size: 42px; font-weight: 400;
    margin-right: 2px;
  }
  /* Front of card */
  .card-front { top: 640px; background: var(--paper); }
  .front-shapes { position: absolute; inset: 0; }
  .front-mark {
    position: absolute; left: 170px; top: 100px;
    display: flex; align-items: center; gap: 20px;
    white-space: nowrap;
  }
  .front-dot { width: 90px; height: 90px; border-radius: 50%; background: var(--leaf); flex: none; }
  .front-name {
    font-family: "Marck Script", cursive;
    font-size: 66px; color: var(--ink);
  }
</style>
</head>
<body>

<section class="card card-back" aria-label="Business card back">
  <div class="back-band"></div>
  <div class="watermark-art" role="img" aria-label="Faint line illustration of a horse among leaves"></div>
  <div class="brand-mark">
    <span class="brand-dot"></span>
    <span class="brand-name">Birchwood Clover</span>
  </div>
  <ul class="contact-list">
    <li class="contact-item">
      <span class="contact-icon">
        <svg viewBox="0 0 24 24" aria-hidden="true"><path fill="#2bb08f" d="M6.6 10.8a15.1 15.1 0 0 0 6.6 6.6l2.2-2.2a1 1 0 0 1 1-.25 11.4 11.4 0 0 0 3.6.57 1 1 0 0 1 1 1V20a1 1 0 0 1-1 1A17 17 0 0 1 3 4a1 1 0 0 1 1-1h3.5a1 1 0 0 1 1 1c0 1.25.2 2.45.57 3.57a1 1 0 0 1-.25 1z"/></svg>
      </span>
      555-218-3946
    </li>
    <li class="contact-item">
      <span class="contact-icon plain"><span class="inner"></span></span>
      @birchwoodclover
    </li>
  </ul>
  <ul class="hay-list">
    <li class="hay-item"><span class="initial">O</span>rchardgrass Hay</li>
    <li class="hay-item"><span class="initial">A</span>lfalfa Hay</li>
    <li class="hay-item"><span class="initial">M</span>ixed Grass Hay</li>
    <li class="hay-item"><span class="initial">P</span>remium Quality Hay</li>
  </ul>
</section>

<section class="card card-front" aria-label="Business card front">
  <svg class="front-shapes" viewBox="0 0 840 480" aria-hidden="true">
    <path d="M0 0 H40 Q150 200 110 480 H0 Z" fill="var(--teal)"/>
    <ellipse cx="520" cy="470" rx="250" ry="150" fill="var(--leaf)"/>
  </svg>
  <div class="front-mark">
    <span class="front-dot"></span>
    <span class="front-name">Birchwood Clover</span>
  </div>
</section>

</body>
</html>
```